Short term Rentals Marketing agency needs Web design.

We Need a web design for our new company based in Calgary, AB. We are a International Luxury home sharing company (short term rental properties, Villas, Boutique Hotels, Bed & Breakfast, Realtors, Mortgage Brokers). We would like to see designs that look simple, modern and professional. Colors would be bold (red, black, white). The final design should communicate something welcoming, symbolize innovation, and growth. Our goal is to form partnerships with Real Estate, Property Management, Short term Rental Clients to make their lives easier and increase revenue. Vlto Harbor Co. offers a flexible and secure way to market our clients properties while maintaining client satisfaction and amazing customer service. We like how https://brinkleafpromo.ca/ is interactive (when you scroll down, text gets larger). Other similar websites for Short Term Rentals is https://www.quillnestgroup.com/, https://dwelvaroo.com/, https://www.kipmarsh.com/, https://www.tarnpenny.com/about-us/, https://vantrelstays.com. We have attached our Logo.

Target Market(s)

short term rental properties, Villas, Boutique Hotels, Bed & Breakfast, Realtors, Mortgage Brokers, property owners

Industry/Entity Type

Real Estate

Coding

Coded - Design and coding required

Number of Pages Required

5+ page

Font styles to use
Sans Serif

Requirements
Must have
• Home Page, About Us page, How it works, Services, Contact us.

We like how https://brinkleafpromo.ca/ is interactive (when you scroll down, text gets larger).

We have attached our Webcopy. We would like Call to Action Buttons where they're located in the copy and page.

Must have our Logo Colors.

Other similar websites for Short Term Rentals is https://www.quillnestgroup.com/, https://dwelvaroo.com/, https://www.kipmarsh.com/, https://www.tarnpenny.com/about-us/, https://vantrelstays.com.
Nice to have
• Catchy, Interactive Home page.

Should not have
• Should not be too cluttered

```html
<!DOCTYPE html>
<html lang="en">
<head>
<meta charset="utf-8">
<title>Vlto Harbor Co. — Partner With Us</title>
<link rel="stylesheet" href="https://fonts.googleapis.com/css2?family=Open+Sans:wght@400;600;700&display=swap">
<style>
:root{
  --red:#e3211f;
  --red-dark:#c91a18;
  --ink:#2b2b2b;
  --text:#4a4a4a;
  --white:#ffffff;
  --muted:#8a8a8a;
  --rule:#e6e6e6;
}
*{margin:0;padding:0;box-sizing:border-box}
html,body{width:1200px;height:3000px;overflow:hidden}
body{font-family:"Open Sans",Arial,sans-serif;color:var(--text);background:var(--white);position:relative}

.site-header{position:absolute;top:0;left:0;width:1200px;height:72px;background:var(--white);display:flex;align-items:center;justify-content:space-between;padding:0 48px;border-bottom:1px solid var(--rule)}
.brand{display:flex;align-items:center;gap:10px;font-weight:700;font-size:22px;color:var(--ink);text-decoration:none}
.brand-mark{width:26px;height:26px;background:var(--red)}
.main-nav{display:flex;gap:34px}
.main-nav a{font-size:12px;font-weight:600;letter-spacing:.06em;color:var(--ink);text-decoration:none;padding:26px 0;border-top:3px solid transparent}
.main-nav a.is-active{color:var(--red);border-top-color:var(--red)}

.hero{position:absolute;top:72px;left:0;width:1200px;height:600px;background:linear-gradient(180deg,#8fb7d4 0%,#b9d3e3 35%,#6e8f9c 55%,#2a8fc0 72%,#137bb4 100%)}
.hero-content{position:absolute;top:0;left:0;width:100%;height:100%;text-align:center;color:var(--white)}
.hero h1{position:absolute;top:130px;left:0;width:100%;font-size:56px;line-height:66px;font-weight:700;letter-spacing:.01em;text-transform:uppercase;text-shadow:0 2px 12px rgba(0,0,0,.25)}
.hero p{position:absolute;top:290px;left:330px;width:540px;font-size:15px;line-height:24px}
.btn-outline-light{position:absolute;top:390px;left:500px;width:200px;height:56px;border:2px solid var(--white);color:var(--white);font-size:12px;font-weight:700;letter-spacing:.08em;display:flex;align-items:center;justify-content:center;text-decoration:none}

.intro{position:absolute;top:740px;left:232px;width:736px;text-align:center;font-size:16px;line-height:27px}
.intro-rule{position:absolute;top:960px;left:510px;width:180px;height:2px;background:var(--red)}
.intro-second{top:1012px}

.feature{position:absolute;left:0;width:1200px}
.feature h2{font-size:52px;line-height:62px;font-weight:600;color:var(--ink)}
.feature p{font-size:16px;line-height:27px;margin-bottom:26px}
.feature-photo{position:absolute;width:360px;height:360px;border-radius:50%}

.feature-revenue{top:1250px}
.feature-revenue .feature-text{position:absolute;left:48px;top:20px;width:660px}
.feature-revenue h2{margin-bottom:64px}
.feature-revenue .feature-photo{left:780px;top:0;background:radial-gradient(circle at 40% 40%,#f1f1f1 0%,#c9c9c9 40%,#5a5a5a 75%,#2f2f2f 100%)}

.feature-support{top:1860px}
.feature-support .feature-photo{left:48px;top:0;background:radial-gradient(circle at 55% 45%,#f6f3e8 0%,#e7d9a8 35%,#b9b2a8 65%,#6f6a66 100%)}
.feature-support .feature-text{position:absolute;left:496px;top:40px;width:660px}
.feature-support h2{margin-bottom:36px}

.feature-risk{top:2290px}
.feature-risk .feature-text{position:absolute;left:48px;top:60px;width:660px}
.feature-risk h2{margin-bottom:40px}
.feature-risk .feature-photo{left:780px;top:0;background:linear-gradient(180deg,#9cc5e6 0%,#cfe2f0 45%,#e9e9e6 60%,#7f8a78 100%)}
.btn-outline-red{position:absolute;left:48px;top:2370px;width:190px;height:58px;border:2px solid var(--red);color:var(--red);font-size:12px;font-weight:700;letter-spacing:.08em;display:flex;align-items:center;justify-content:center;text-decoration:none}

.site-footer{position:absolute;top:2800px;left:0;width:1200px;height:200px;background:var(--red);color:var(--white)}
.footer-brand{position:absolute;left:108px;top:70px;display:flex;align-items:center;gap:12px;font-size:30px;font-weight:700;color:var(--white)}
.footer-brand .brand-mark{width:34px;height:34px;background:var(--white)}
.footer-col{position:absolute;top:54px;font-size:12px;line-height:22px}
.footer-col h3{font-size:12px;font-weight:700;letter-spacing:.06em;margin-bottom:6px;text-transform:uppercase}
.footer-contact{left:690px}
.footer-learn{left:840px}
.footer-social{position:absolute;left:980px;top:52px;display:flex;gap:16px}
.footer-social span{width:18px;height:18px;border-radius:50%;background:var(--white)}
</style>
</head>
<body>

<header class="site-header">
  <a class="brand" href="#"><span class="brand-mark"></span>Vlto Harbor Co.</a>
  <nav class="main-nav">
    <a class="is-active" href="#">HOME</a>
    <a href="#">ABOUT US</a>
    <a href="#">HOW IT WORKS</a>
    <a href="#">SERVICES</a>
    <a href="#">CONTACT US</a>
  </nav>
</header>

<section class="hero" role="img" aria-label="Luxury villa terrace with an infinity pool overlooking the sea under a blue sky">
  <div class="hero-content">
    <h1>Partner With Us And<br>Let's Start Growing</h1>
    <p>Reach out to find out about how we can help your short-term rental reach its full potential and grow your income.</p>
    <a class="btn-outline-light" href="#">WORK WITH US</a>
  </div>
</section>

<p class="intro">Vlto Harbor Co. is here to manage and market your short-term rental properties so you don't have to. Enjoy peace of mind in knowing your short-term rental properties, vacation homes, villas, hotels, and B&amp;Bs are safe, secure, and profitable – no matter where you are in the world. We will help you market, manage, and capitalize on everything, from your newest bookings to house cleaning and upkeep.</p>
<div class="intro-rule"></div>
<p class="intro intro-second">Vlto Harbor Co. saves you time, money, and effort, so that you can focus on the things that matter most to you. Let us help you increase your rental revenue in a simple and hassle-free way by increasing your occupancy, streamlining your bookings, getting you amazing exposure, and keeping your property looking incredible year-round.</p>

<section class="feature feature-revenue">
  <div class="feature-text">
    <h2>Increase Your Revenue<br>(without the hassle)</h2>
    <p>Having Vlto Harbor Co. manage and market your rental property lets you benefit from increased revenues without having to put in the hours of work yourself. Vlto Harbor Co. will manage your property listings, advertise your listings, optimize your rental pricing, increase your occupancy, and help you offer the very best customer experience.</p>
    <p>We won't charge you a fixed monthly retainer! Instead, we work on a commission-based system to give you a great hands-off opportunity. We charge 30% of the gross revenue your unit brings in per month. For example, if we've made $1,000,000 in a month on your property, you'll take home $700,000 and we'll only take $300,000!</p>
  </div>
  <div class="feature-photo" role="img" aria-label="Hands working on a laptop showing booking analytics"></div>
</section>

<section class="feature feature-support">
  <div class="feature-photo" role="img" aria-label="Team meeting at a table beside a wall of sticky notes"></div>
  <div class="feature-text">
    <h2>Receive Constant Support</h2>
    <p>Our dedicated team is there to take care of your property so that you don't have to. Our affordable and professional services include being there to support your guests, constant technical communication, and on-site operations management.</p>
  </div>
</section>

<section class="feature feature-risk">
  <div class="feature-text">
    <h2>Manage Your Risks and<br>Insurance</h2>
    <p>Vlto Harbor Co. will help you protect your property income by giving you the security and insurance you need when it comes to pricing and managing your security deposits. Please note that terms and conditions apply.</p>
  </div>
  <div class="feature-photo" role="img" aria-label="Modern white villa with a pool under a clear sky"></div>
  <a class="btn-outline-red" href="#">WORK WITH US</a>
</section>

<footer class="site-footer">
  <div class="footer-brand"><span class="brand-mark"></span>Vlto Harbor Co.</div>
  <div class="footer-col footer-contact">
    <h3>Contact Us</h3>
    <div>+1 403 555 0142</div>
    <div>hello@vltoharbor.ca</div>
  </div>
  <div class="footer-col footer-learn">
    <h3>Learn More</h3>
    <div>Home</div>
    <div>About Us</div>
    <div>How it Works</div>
    <div>Services</div>
    <div>Contact Us</div>
  </div>
  <div class="footer-social" aria-label="Social links">
    <span></span><span></span><span></span>
  </div>
</footer>

</body>
</html>
```